Bakery Business Cards

We are in need of business cards for our bakery business--something non-generic that reflects our business and will stand out. We are a wholesale bakery that primarily services in-store bakeries, casinos, schools, distributors, and fund-raising companies. The family business was founded in 1960. (www.marlowsovenworks.com)

```html
<!DOCTYPE html>
<html lang="en">
<head>
<meta charset="utf-8">
<title>Marlow's Ovenworks — Business Cards</title>
<link rel="stylesheet" href="https://fonts.googleapis.com/css2?family=Libre+Baskerville:wght@400;700&display=swap">
<style>
  :root {
    --bg: #1b1b1d;
    --card-white: #ffffff;
    --brand-blue: #2a50a3;
    --text-grey: #5a5a5a;
    --rule-grey: #9a9a9a;
  }
  * { box-sizing: border-box; margin: 0; padding: 0; }
  html, body { width: 1200px; height: 936px; overflow: hidden; }
  body {
    background: var(--bg);
    font-family: "Libre Baskerville", Georgia, serif;
    position: relative;
  }
  .card {
    position: absolute;
    left: 290px;
    width: 620px;
    height: 354px;
    box-shadow: 0 14px 30px rgba(0,0,0,.55);
  }
  .card--front { top: 100px; background: var(--card-white); }
  .card--back  { top: 482px; background: var(--brand-blue); }

  .brand-name {
    font-family: "Libre Baskerville", Georgia, serif;
    font-weight: 400;
    line-height: 1.1;
  }
  .card--front .brand-name {
    position: absolute; left: 44px; top: 56px;
    font-size: 30px; color: var(--brand-blue);
  }
  .brand-since {
    display: block; margin-top: 10px;
    font-size: 13px; letter-spacing: .12em; text-transform: uppercase;
  }

  .accent-tab {
    position: absolute; right: 0; top: 118px;
    width: 14px; height: 38px; background: var(--brand-blue);
  }
  .person {
    position: absolute; right: 44px; top: 122px; text-align: right;
  }
  .person__name { font-size: 26px; color: var(--brand-blue); }
  .person__title { font-size: 13px; color: var(--text-grey); margin-top: 4px; letter-spacing: .05em; }

  .divider {
    position: absolute; left: 112px; right: 24px; top: 214px;
    height: 1px; background: var(--rule-grey);
  }
  .contact-list {
    position: absolute; left: 118px; top: 234px; list-style: none;
    font-size: 14px; color: var(--text-grey); line-height: 1.75;
  }
  .contact-list li { display: flex; align-items: center; gap: 8px; }
  .contact-list svg { width: 11px; height: 11px; fill: var(--brand-blue); flex: none; }
  .address {
    position: absolute; right: 44px; top: 234px; text-align: right;
    font-style: normal; font-size: 14px; color: var(--text-grey); line-height: 1.75;
  }

  .card--back .brand-name {
    position: absolute; left: 0; right: 0; top: 112px; text-align: center;
    font-size: 44px; color: var(--card-white);
  }
  .card--back .brand-since { font-size: 16px; margin-top: 14px; }
</style>
</head>
<body>
  <section class="card card--front">
    <div class="brand-name">Marlow's<br>Ovenworks<span class="brand-since">Since 1960</span></div>
    <div class="accent-tab"></div>
    <div class="person">
      <div class="person__name">Daniel Harper</div>
      <div class="person__title">CEO</div>
    </div>
    <div class="divider"></div>
    <ul class="contact-list">
      <li><svg viewBox="0 0 24 24"><path d="M6.6 10.8a15 15 0 0 0 6.6 6.6l2.2-2.2c.3-.3.7-.4 1-.2 1.1.4 2.3.6 3.6.6.6 0 1 .4 1 1V20c0 .6-.4 1-1 1A17 17 0 0 1 3 4c0-.6.4-1 1-1h3.5c.6 0 1 .4 1 1 0 1.3.2 2.5.6 3.6.1.3 0 .7-.2 1z"/></svg>405.555.0142</li>
      <li><svg viewBox="0 0 24 24"><path d="M2 5h20v14H2z M2 5l10 8 10-8" /></svg>contact@marlowsovenworks.com</li>
      <li><svg viewBox="0 0 24 24"><circle cx="12" cy="12" r="10"/></svg>www.marlowsovenworks.com</li>
    </ul>
    <address class="address">P.O Box 620318<br>Cedar Ridge, OK 73190</address>
  </section>

  <section class="card card--back">
    <div class="brand-name">Marlow's Ovenworks<span class="brand-since">Since 1960</span></div>
  </section>
</body>
</html>
```